Business Card Design Project

We have a logo design and are now looking for a business card design. We supply pre-construction services to the Wireless Telecommunication Industry in the development of cell phone tower and other antenna supporting infrastructure e.g. buildings. The types of services include Real Estate Leasing, Zoning & Permitting,Surveying and A&E work. I am looking for a card that includes the logo we have selected along with the full company name. Company colors are Blue and Silver. I want something professional and that "pops". Use your imagination with the four sided star portion of the logo - it can be stretched such that it occupies a large portion of the card or kept simple the way it is. I am interested in seeing the design on a white, silver, navy, black or charcoal background or any other color you think works well with the logo. Apart from the logo that includes HRM we also need to see the full company name on the card - Harborline Relay Maintenance, Inc. The design must also show a persons name, title, address, (2) phone numbers, e-mail address and web address www.hrm.example

Target Market(s)

Cell phone carriers e.g. Quellport Mobile, BN&K, Zandex Cell, Ovalo etc.

Industry/Entity Type

Cell Phone

Requirements
Must have
• Logo and
Harborline Relay Maintenance, Inc.

```html
<!DOCTYPE html>
<html lang="en">
<head>
<meta charset="utf-8">
<title>Harborline Relay Maintenance, Inc. — Business Card</title>
<link rel="stylesheet" href="https://fonts.googleapis.com/css2?family=Arimo:ital,wght@0,400;0,700;1,400&display=swap">
<style>
  :root {
    --navy-deep: #1b3770;
    --navy: #24437c;
    --steel: #5d7196;
    --mist: #b4bccd;
    --glow: #e3e7ef;
    --silver: #c9ced6;
    --brand-blue: #3a8fe0;
    --text-white: #ffffff;
    --text-soft: #d9dde5;
  }
  html, body {
    margin: 0;
    padding: 0;
    width: 1200px;
    height: 720px;
    overflow: hidden;
    background: #ffffff;
  }
  .card {
    position: relative;
    width: 1200px;
    height: 720px;
    overflow: hidden;
    font-family: "Arimo", Arial, sans-serif;
    color: var(--text-white);
    background:
      radial-gradient(ellipse 620px 520px at 1110px 640px, var(--glow) 0%, var(--mist) 28%, rgba(93,113,150,0.6) 58%, rgba(36,67,124,0) 100%),
      linear-gradient(118deg, var(--navy-deep) 0%, var(--navy) 48%, var(--steel) 78%, var(--mist) 100%);
  }
  .brand-mark {
    position: absolute;
    left: 70px;
    top: 92px;
    display: flex;
    align-items: center;
    gap: 28px;
  }
  .brand-mark__dot {
    width: 120px;
    height: 120px;
    border-radius: 50%;
    background: var(--brand-blue);
  }
  .brand-mark__name {
    font-size: 150px;
    font-weight: 700;
    line-height: 1;
    letter-spacing: 4px;
    color: var(--silver);
  }
  .company-name {
    position: absolute;
    left: 70px;
    top: 308px;
    margin: 0;
    font-size: 41px;
    font-weight: 400;
    font-style: italic;
    color: var(--text-soft);
    white-space: nowrap;
  }
  .contact {
    position: absolute;
    left: 200px;
    top: 396px;
  }
  .contact__person {
    margin: 0;
    font-size: 40px;
    font-weight: 700;
    white-space: nowrap;
  }
  .contact__title {
    margin-left: 30px;
    font-size: 24px;
    font-weight: 400;
    font-style: italic;
  }
  .contact__phones {
    display: flex;
    gap: 90px;
    margin: 22px 0 0;
    font-size: 28px;
  }
  .contact__email {
    margin: 22px 0 0;
    font-size: 38px;
  }
  .contact__web {
    margin: 20px 0 0;
    font-size: 38px;
    font-weight: 700;
  }
</style>
</head>
<body>
  <main class="card">
    <div class="brand-mark">
      <span class="brand-mark__dot" aria-hidden="true"></span>
      <span class="brand-mark__name">HRM</span>
    </div>

    <h1 class="company-name">Harborline Relay Maintenance, Inc.</h1>

    <section class="contact">
      <p class="contact__person">John Citizen<span class="contact__title">title</span></p>
      <p class="contact__phones"><span>ph 1234 5678</span><span>ph 8765 4321</span></p>
      <p class="contact__email">johncitizen@mail.example</p>
      <p class="contact__web">www.hrm.example</p>
    </section>
  </main>
</body>
</html>
```